R. Korvane & Korvane----- Truck repair shop, specialized in Heavy Duty truck Engines and maintance

First of all, I am looking for the perfect logo. In other words, I want a simple and easy to remember. Nowadays, diesel engines have accomplished much technological progress in emission reductions. As a manager, I understand that technology is an important tool in this industry. I don't want the usual logo that I see in shops such as trucks, pistons, wrenches. I want a logo and then a phrase saying specialists in Diesel Engines.

Target Market(s)

Truck Drivers, logistic companies, fleet

Contact Information for Business Card

Simple. Easy logo to remember.

Font styles to use
Serif

Colors

Designer to choose colors to be used in the design.

Requirements
Must have
• Business name
• Address 482 Marlow Avenue Brackton 07391 NJ
• Phone number
• email: rkorvaneandkorvane@brinmail.com
Nice to have
• the Name should be " R. Korvane & Korvane " not R. Korvane AND Korvane
Should not have
• card should not have the usual logos of mechanic shops. e.g. cars, trucks, just a Logo

```html
<!DOCTYPE html>
<html lang="en">
<head>
<meta charset="utf-8">
<title>R. Korvane &amp; Korvane — Business Card</title>
<link rel="stylesheet" href="https://fonts.googleapis.com/css2?family=Cormorant+Garamond:wght@600;700&family=Crimson+Text:wght@400;600;700&display=swap">
<style>
  :root {
    --backdrop: #2b2b2b;
    --card-black: #0d0d0d;
    --card-white: #ffffff;
    --gold: #f0b323;
    --ink: #1c1c1c;
    --soft-ink: #3a3a3a;
    --divider: #d4d4d4;
    --tagline-light: #f2f2f2;
  }
  * { box-sizing: border-box; margin: 0; padding: 0; }
  html, body {
    width: 1200px; height: 660px; overflow: hidden;
    background: var(--backdrop);
  }
  .stage {
    width: 1200px; height: 660px;
    display: flex; align-items: center; justify-content: center; gap: 40px;
  }
  .card {
    width: 540px; height: 309px; position: relative; overflow: hidden;
    box-shadow: 0 14px 30px rgba(0,0,0,.45);
  }
  .card--front { background: var(--card-black); display: flex; align-items: center; justify-content: center; }
  .card--back { background: var(--card-white); }

  .brand { display: flex; flex-direction: column; align-items: center; }
  .brand__dot {
    width: 34px; height: 34px; border-radius: 50%;
    background: var(--gold); margin-bottom: 14px;
  }
  .brand__name {
    font-family: "Cormorant Garamond", serif; font-weight: 700;
    font-size: 34px; line-height: 1; color: var(--gold); white-space: nowrap;
  }
  .brand__tagline {
    font-family: "Crimson Text", serif; font-weight: 600;
    font-size: 12px; letter-spacing: 0.62em; margin-top: 8px; margin-right: -0.62em;
    text-transform: uppercase; white-space: nowrap;
  }
  .card--front .brand__tagline { color: var(--tagline-light); }
  .card--back .brand__tagline { color: var(--ink); }
  .card--back .brand__name { font-size: 27px; }
  .card--back .brand__dot { width: 28px; height: 28px; margin-bottom: 12px; }
  .card--back .brand__tagline { font-size: 10px; }

  .band { position: absolute; left: 0; right: 0; background: var(--card-black); }
  .band--top { top: 0; height: 12px; border-bottom: 4px solid var(--gold); }
  .band--bottom { bottom: 0; height: 20px; border-top: 4px solid var(--gold); }

  .back__brand {
    position: absolute; left: 0; top: 16px; bottom: 24px; width: 270px;
    display: flex; align-items: center; justify-content: center;
  }
  .back__divider {
    position: absolute; left: 270px; top: 40px; bottom: 48px;
    width: 1px; background: var(--divider);
  }
  .contact {
    position: absolute; left: 296px; top: 78px;
    font-family: "Crimson Text", serif; color: var(--soft-ink);
  }
  .contact__name { font-size: 18px; font-weight: 700; color: var(--ink); line-height: 1.05; }
  .contact__title { font-size: 13px; color: var(--gold); margin-bottom: 8px; }
  .contact__row { display: flex; align-items: center; gap: 8px; font-size: 13.5px; line-height: 1.45; }
  .contact__row svg { width: 12px; height: 12px; flex: none; }
  .contact__address { font-size: 13.5px; line-height: 1.25; margin-top: 6px; }
</style>
</head>
<body>
<main class="stage">
  <section class="card card--front" aria-label="Business card front">
    <div class="brand">
      <span class="brand__dot"></span>
      <span class="brand__name">R. Korvane &amp; Korvane</span>
      <span class="brand__tagline">Diesel Engines</span>
    </div>
  </section>

  <section class="card card--back" aria-label="Business card back">
    <div class="band band--top"></div>
    <div class="back__brand">
      <div class="brand">
        <span class="brand__dot"></span>
        <span class="brand__name">R. Korvane &amp; Korvane</span>
        <span class="brand__tagline">Diesel Engines</span>
      </div>
    </div>
    <div class="back__divider"></div>
    <div class="contact">
      <p class="contact__name">Your Name</p>
      <p class="contact__title">Title</p>
      <p class="contact__row">
        <svg viewBox="0 0 12 12" aria-hidden="true"><rect x="2.5" y="0.5" width="7" height="11" rx="1.2" fill="none" stroke="var(--gold)" stroke-width="1.2"/><rect x="4.5" y="9" width="3" height="1" fill="var(--gold)"/></svg>
        201.555.0148
      </p>
      <p class="contact__row">
        <svg viewBox="0 0 12 12" aria-hidden="true"><rect x="0.5" y="2" width="11" height="8" fill="var(--gold)"/><path d="M0.8 2.3 6 6.6 11.2 2.3" fill="none" stroke="#fff" stroke-width="1"/></svg>
        rkorvaneandkorvane@brinmail.com
      </p>
      <p class="contact__address">Address 482 Marlow Avenue<br>Brackton 07391 NJ</p>
    </div>
    <div class="band band--bottom"></div>
  </section>
</main>
</body>
</html>
```